Design Executive Business Acquisitons Brokerage Website

Modern but Professional with the colours black, purple and white. Must convey authenticity, and progressive out-of-square thinking. We are a boutique Business Broking firm located in Brisbane QLD Australia. We market and sell businesses with sales revenue/turnover from Au $1M to $15 M + or have a minimum staff of 15 to 50 staff. Our buyers are generally acquisitions corporate buyers. We need a modern approach but conservative tones. We are serious and experienced. We say it as it is and we get the job done! We sell in the following industries but not limited to, engineering, manufacturing, agriculture, recruitment, transportation, warehousing, services, IT,eCommerce, civil construction,mining, wholesaling, dealerships, MEdical (all), service stations, Management rights, high-end retail, building construction,importing,exporting to name a few.

Target Market(s)

SME Corporate Public & Private exsisting large businesses that are looking to buy through acquisitions

Industry/Entity Type

Coommercial executive Business Sale

Number of Pages Required

5+ page

Font styles to use
Sans Serif

Requirements
Must have
• Serious tones, searchar, NDA form, serious corporate executive feel. Include all corporaate colors,black less whit purples.Corporate Logo
Nice to have
• carosel moving right to left of industry pictures as per above and attached industries
Should not have
• No hand shaking, business people.

```html
<!DOCTYPE html>
<html lang="en">
<head>
<meta charset="utf-8">
<title>Meridian Acquisitions Group</title>
<link href="https://fonts.googleapis.com/css2?family=Poppins:ital,wght@0,400;0,500;0,600;0,700;1,400&family=Open+Sans:wght@400;600;700&display=swap" rel="stylesheet">
<style>
:root{
  --purple:#5a3a8a;
  --purple-dark:#3e2468;
  --ink:#1f1f1f;
  --text:#666;
  --soft:#f6f6f8;
  --white:#fff;
  --footer-bar:#2f2f33;
}
*{box-sizing:border-box;margin:0;padding:0}
html,body{width:1200px;height:4277px;overflow:hidden}
body{position:relative;background:var(--white);font-family:"Open Sans",sans-serif;color:var(--ink)}
.abs{position:absolute}
.h-font{font-family:"Poppins",sans-serif}
.accent{color:var(--purple)}
.blob{position:absolute;border-radius:50%;background:var(--soft)}
/* header */
.brand{left:46px;top:30px;display:flex;align-items:center;gap:10px}
.brand-dot{width:40px;height:40px;border-radius:50%;background:var(--purple)}
.brand-name{font-family:"Poppins",sans-serif;font-weight:600;font-size:20px;color:var(--purple);line-height:1.05;width:170px}
.nav{top:46px;font-size:13px;color:#333;font-family:"Open Sans",sans-serif}
.nav.active{color:var(--purple)}
.btn{position:absolute;display:flex;align-items:center;justify-content:center;border-radius:30px;font-family:"Poppins",sans-serif;font-weight:600;font-size:12px;text-transform:uppercase;color:var(--white);background:var(--purple)}
.btn.dark{background:var(--ink)}
.btn.light{background:var(--white);color:var(--purple-dark)}
.circle{position:absolute;border-radius:50%;border:1.5px solid #bbb;display:flex;align-items:center;justify-content:center;background:var(--white)}
.kicker{font-family:"Poppins",sans-serif;font-size:20px;color:var(--ink)}
.title{font-family:"Poppins",sans-serif;font-weight:700;font-size:52px;line-height:1.2;color:var(--ink)}
.para{font-size:12.5px;line-height:25px;color:var(--text)}
.photo{position:absolute}
.card{position:absolute;width:310px;background:var(--white);box-shadow:0 10px 30px rgba(0,0,0,.08)}
.card h3{font-family:"Poppins",sans-serif;font-weight:500;font-size:21px;color:var(--ink)}
.card p{font-size:12.5px;line-height:22px;color:var(--text)}
.purple-band{left:0;top:1962px;width:1200px;height:827px;border-top-right-radius:110px;background:linear-gradient(135deg,#5d3c90,#3f2468)}
.sale h4{font-family:"Poppins",sans-serif;font-weight:600;font-size:30px;color:var(--purple)}
.sale h3{font-family:"Poppins",sans-serif;font-weight:600;font-size:21px;margin-top:18px}
.more{font-family:"Poppins",sans-serif;font-weight:600;font-size:14px;color:var(--ink);display:flex;align-items:center;gap:10px}
.footer{left:0;top:3826px;width:1200px;height:401px;border-top-right-radius:110px;background:linear-gradient(135deg,#5d3c90,#4a2c78);color:var(--white)}
.footer h5{font-family:"Poppins",sans-serif;font-weight:500;font-size:16px}
.footer li{list-style:none;font-size:11.5px;line-height:22.5px}
.bar{left:0;top:4227px;width:1200px;height:50px;background:var(--footer-bar);color:var(--white);font-size:11px}
</style>
</head>
<body>

<div class="blob" style="left:-260px;top:-120px;width:700px;height:700px"></div>
<div class="blob" style="left:-120px;top:440px;width:360px;height:300px"></div>
<div class="blob" style="left:1080px;top:1000px;width:400px;height:500px"></div>
<div class="blob" style="left:-200px;top:1500px;width:500px;height:500px"></div>
<div class="blob" style="left:300px;top:3180px;width:1000px;height:600px"></div>

<!-- header -->
<div class="abs brand"><span class="brand-dot"></span><span class="brand-name">Meridian Acquisitions Group</span></div>
<div class="abs nav active" style="left:400px">Home</div>
<div class="abs nav" style="left:465px">Our Services</div>
<div class="abs nav" style="left:573px">About Us</div>
<div class="abs nav" style="left:661px">Business For Sale</div>
<div class="abs nav" style="left:798px">Blog</div>
<div class="abs nav" style="left:855px">Contact Us</div>
<svg class="abs" style="left:953px;top:47px" width="16" height="16" viewBox="0 0 16 16"><circle cx="7" cy="7" r="5" fill="none" stroke="#333" stroke-width="1.6"/><path d="M11 11l4 4" stroke="#333" stroke-width="1.6"/></svg>
<div class="btn" style="left:1004px;top:37px;width:145px;height:38px;text-transform:none;font-weight:500">
  <svg width="12" height="12" viewBox="0 0 24 24" style="margin-right:8px"><path fill="#fff" d="M6.6 10.8a15 15 0 006.6 6.6l2.2-2.2c.3-.3.7-.4 1-.2 1.1.4 2.3.6 3.6.6.6 0 1 .4 1 1V20c0 .6-.4 1-1 1A17 17 0 013 4c0-.6.4-1 1-1h3.5c.6 0 1 .4 1 1 0 1.3.2 2.5.6 3.6.1.3 0 .7-.2 1z"/></svg>+61 70000000</div>

<!-- hero -->
<div class="abs kicker" style="left:100px;top:203px">#1 Broker in the Country</div>
<div class="abs title" style="left:100px;top:238px;font-size:54px;line-height:63px">
  <span class="accent">Sell Your Business</span><br>&amp; Start Your<br>Next Adventure</div>
<div class="btn" style="left:100px;top:475px;width:182px;height:41px">Read More</div>
<div class="btn dark" style="left:296px;top:475px;width:184px;height:41px">Contact Us</div>
<div class="circle" style="left:100px;top:626px;width:38px;height:38px"></div>
<div class="circle" style="left:148px;top:626px;width:38px;height:38px"></div>
<div class="circle" style="left:196px;top:626px;width:38px;height:38px"></div>
<div class="circle" style="left:244px;top:626px;width:38px;height:38px"></div>
<div class="photo" role="img" aria-label="Smiling businessman in a dark suit holding a coffee cup outside an office building" style="left:616px;top:108px;width:483px;height:556px;border-bottom-right-radius:90px;background:linear-gradient(135deg,#7d9ab8,#3a4c64 60%,#1e2533)"></div>
<div class="circle" style="left:1109px;top:360px;width:40px;height:40px;border-color:#555">
  <svg width="16" height="16" viewBox="0 0 16 16"><path d="M2 8h12M9 3l5 5-5 5" fill="none" stroke="#333" stroke-width="1.5"/></svg></div>

<!-- services -->
<div class="abs kicker" style="left:103px;top:768px;font-size:17px">What We Do</div>
<div class="abs title" style="left:103px;top:790px;font-size:50px"><span class="accent">Our</span> Services</div>
<div class="abs para" style="left:100px;top:863px;width:600px;font-size:12px;line-height:23px">Lorem ipsum dolor sit amet, consectetur adipiscing elit, sed do eiusmod tempor incididunt magna aliqua. Ut enim ad minim veniam, quis nostrud exercitation ullamco laboris.</div>
<div class="btn" style="left:918px;top:862px;width:181px;height:43px">Read More</div>

<div class="circle" style="left:50px;top:1064px;width:38px;height:38px"><svg width="16" height="16" viewBox="0 0 16 16"><path d="M14 8H2M7 3L2 8l5 5" fill="none" stroke="#555" stroke-width="1.5"/></svg></div>
<div class="circle" style="left:1110px;top:1064px;width:38px;height:38px"><svg width="16" height="16" viewBox="0 0 16 16"><path d="M2 8h12M9 3l5 5-5 5" fill="none" stroke="#555" stroke-width="1.5"/></svg></div>

<div class="card" style="left:100px;top:956px;height:256px;border-bottom-right-radius:40px;padding:50px 28px 0">
  <svg width="48" height="44" viewBox="0 0 48 44"><rect x="2" y="2" width="26" height="40" fill="none" stroke="var(--purple)" stroke-width="3"/><rect x="28" y="14" width="18" height="28" fill="none" stroke="var(--purple)" stroke-width="3"/><g fill="var(--purple)"><rect x="8" y="9" width="5" height="5"/><rect x="17" y="9" width="5" height="5"/><rect x="8" y="19" width="5" height="5"/><rect x="17" y="19" width="5" height="5"/><rect x="8" y="29" width="5" height="5"/><rect x="17" y="29" width="5" height="5"/><rect x="34" y="22" width="5" height="5"/><rect x="34" y="31" width="5" height="5"/></g></svg>
  <h3 style="margin-top:18px">Selling Business</h3>
  <p style="margin-top:10px">Lorem ipsum dolor sit amet, consectetur adipiscing elit, sed do eiusmod tempor incididunt ut labore et dolore...</p></div>
<div class="card" style="left:445px;top:956px;height:256px;border-top-left-radius:40px;padding:50px 28px 0;background:linear-gradient(135deg,#5d3c90,#40246a)">
  <div class="h-font" style="color:#fff;font-size:44px;font-weight:600;line-height:44px">$</div>
  <h3 style="margin-top:18px;color:#fff">Business Valuation</h3>
  <p style="margin-top:10px;color:#fff">Lorem ipsum dolor sit amet, consectetur adipiscing elit, sed do eiusmod tempor incididunt ut labore et dolore...</p></div>
<div class="card" style="left:789px;top:956px;height:256px;border-top-left-radius:40px;padding:50px 28px 0">
  <svg width="48" height="44" viewBox="0 0 48 44"><text x="18" y="20" font-family="Poppins,sans-serif" font-weight="700" font-size="22" fill="var(--purple)">$</text><path d="M2 32c6-4 12-4 18-1h10c3 0 3 4 0 4H20M2 40h24l16-10c2-2 0-5-3-4l-11 6" fill="none" stroke="var(--purple)" stroke-width="3"/></svg>
  <h3 style="margin-top:18px">Business Acquisition</h3>
  <p style="margin-top:10px">Lorem ipsum dolor sit amet, consectetur adipiscing elit, sed do eiusmod tempor incididunt ut labore et dolore...</p></div>

<!-- about -->
<div class="photo" role="img" aria-label="Team of three business professionals standing in front of a glass office tower" style="left:100px;top:1323px;width:499px;height:526px;border-top-right-radius:80px;border-bottom-left-radius:80px;background:linear-gradient(160deg,#9cb3cc,#4c6784 55%,#23272f)"></div>
<div class="abs kicker" style="left:661px;top:1379px;font-size:17px">Who We Are</div>
<div class="abs title" style="left:661px;top:1400px;font-size:52px;line-height:63px"><span class="accent">Not Your Typical</span><br>Broker Firm</div>
<div class="abs para" style="left:661px;top:1535px;width:440px">Lorem ipsum dolor sit amet, consectetur adipiscing elit, sed do eiusmod tempor incididunt ut labore et dolore magna aliqua. Ut enim ad minim veniam, quis nostrud.</div>
<div class="abs para" style="left:661px;top:1618px;width:440px">exercitation ullamco laboris nisi ut aliquip ex ea commodo consequat. Duis aute irure dolor in reprehenderit in voluptate velit esse cillum dolore eu fugiat nulla pariatur. Excepteur sint occaecat cupidatat non proident, sunt in culpa qui officia deserunt mollit anim id est laborum.</div>
<div class="btn" style="left:661px;top:1751px;width:182px;height:43px">Read More</div>

<!-- business for sale -->
<div class="abs purple-band"></div>
<div class="abs kicker" style="left:0;width:1200px;text-align:center;top:2051px;font-size:17px;color:#fff">Lorum Ipsum</div>
<div class="abs title" style="left:0;width:1200px;text-align:center;top:2073px;color:#fff">Business For Sale</div>
<div class="circle" style="left:54px;top:2297px;width:38px;height:38px;border:none;background:#c9c2d6"><svg width="16" height="16" viewBox="0 0 16 16"><path d="M14 8H2M7 3L2 8l5 5" fill="none" stroke="#555" stroke-width="1.5"/></svg></div>
<div class="circle" style="left:1114px;top:2297px;width:38px;height:38px;border:none;background:#c9c2d6"><svg width="16" height="16" viewBox="0 0 16 16"><path d="M2 8h12M9 3l5 5-5 5" fill="none" stroke="#555" stroke-width="1.5"/></svg></div>

<div class="card sale" style="left:100px;top:2175px;height:292px;border-bottom-right-radius:40px;padding:40px 25px 0">
  <h4>$68,000,000</h4><h3>Geo Drilling Corporation</h3>
  <p style="margin-top:14px">Lorem ipsum dolor sit amet, consectetur adipiscing elit, sed do eiusmod tempor incididunt ut labore....</p>
  <div class="more" style="margin-top:18px">Read More <svg width="16" height="12" viewBox="0 0 16 12"><path d="M1 6h13M9 1l5 5-5 5" fill="none" stroke="#222" stroke-width="2"/></svg></div></div>
<div class="card sale" style="left:450px;top:2175px;height:292px;border-top-left-radius:40px;padding:40px 25px 0">
  <h4>$2,000,000</h4><h3>Restaurant Chain</h3>
  <p style="margin-top:14px">Lorem ipsum dolor sit amet, consectetur adipiscing elit, sed do eiusmod tempor incididunt ut labore....</p>
  <div class="more" style="margin-top:18px">Read More <svg width="16" height="12" viewBox="0 0 16 12"><path d="M1 6h13M9 1l5 5-5 5" fill="none" stroke="#222" stroke-width="2"/></svg></div></div>
<div class="card sale" style="left:789px;top:2175px;height:292px;padding:40px 25px 0">
  <h4>$2,800,000</h4><h3>Ball Manufacturer</h3>
  <p style="margin-top:14px">Lorem ipsum dolor sit amet, consectetur adipiscing elit, sed do eiusmod tempor incididunt ut labore....</p>
  <div class="more" style="margin-top:18px">Read More <svg width="16" height="12" viewBox="0 0 16 12"><path d="M1 6h13M9 1l5 5-5 5" fill="none" stroke="#222" stroke-width="2"/></svg></div></div>
<div class="btn light" style="left:510px;top:2530px;width:180px;height:42px">View More</div>

<!-- testimonial -->
<div class="card" style="left:100px;top:2666px;width:999px;height:402px;border-top-right-radius:90px;text-align:center;padding-top:64px">
  <svg width="54" height="46" viewBox="0 0 54 46"><path fill="var(--purple)" d="M2 2h20v22c0 12-8 20-18 20l-2-6c6-1 9-5 9-10H2zM32 2h20v22c0 12-8 20-18 20l-2-6c6-1 9-5 9-10h-9z"/></svg>
  <p class="h-font" style="font-style:italic;font-size:23px;line-height:38px;color:#333;margin-top:20px">I've met a lot of business brokers... no one's going to work harder<br>for you than this group</p>
  <div role="img" aria-label="Client portrait" style="width:54px;height:54px;border-radius:50%;background:linear-gradient(135deg,#d9c2b0,#7a5b48);margin:16px auto 0"></div>
  <p style="font-size:12px;font-weight:600;margin-top:12px">Daniel Hart - Business Owner</p>
  <div style="display:flex;gap:12px;justify-content:center;margin-top:28px">
    <span style="width:9px;height:9px;border-radius:50%;background:#aaa"></span><span style="width:9px;height:9px;border-radius:50%;background:var(--purple)"></span><span style="width:9px;height:9px;border-radius:50%;background:#aaa"></span><span style="width:9px;height:9px;border-radius:50%;background:#aaa"></span></div>
</div>

<!-- blog -->
<div class="abs kicker" style="left:0;width:1200px;text-align:center;top:3165px;font-size:17px">Our Blog</div>
<div class="abs title" style="left:0;width:1200px;text-align:center;top:3187px"><span class="accent">News</span> &amp; Events</div>
<div class="circle" style="left:50px;top:3527px;width:38px;height:38px"><svg width="16" height="16" viewBox="0 0 16 16"><path d="M14 8H2M7 3L2 8l5 5" fill="none" stroke="#555" stroke-width="1.5"/></svg></div>
<div class="circle" style="left:1110px;top:3527px;width:38px;height:38px"><svg width="16" height="16" viewBox="0 0 16 16"><path d="M2 8h12M9 3l5 5-5 5" fill="none" stroke="#555" stroke-width="1.5"/></svg></div>

<div class="photo" role="img" aria-label="Four colleagues standing outside an office building" style="left:100px;top:3287px;width:310px;height:249px;border-bottom-right-radius:50px;background:linear-gradient(160deg,#c6d0da,#6c7d90 60%,#2c3340)"></div>
<div class="photo" role="img" aria-label="Two colleagues reviewing a tablet in a bright office" style="left:445px;top:3287px;width:310px;height:249px;border-top-left-radius:50px;background:linear-gradient(160deg,#d9d4cc,#8b7c6c 60%,#3a332d)"></div>
<div class="photo" role="img" aria-label="Group of smiling business team members in an office" style="left:789px;top:3287px;width:310px;height:249px;border-bottom-left-radius:50px;background:linear-gradient(160deg,#dfe7ee,#93a6b8 60%,#2e3540)"></div>

<div class="abs" style="left:100px;top:3562px;width:310px">
  <div class="h-font" style="font-size:20px">Lorem ipsum dolor sit amet...</div>
  <div style="font-size:11px;color:#555;margin-top:10px">22 - June - 2022</div>
  <p class="para" style="margin-top:18px;line-height:22px">Lorem ipsum dolor sit amet, consectetur adipiscing elit, sed do eiusmod tempor incididunt ut labore....</p>
  <div class="h-font" style="font-size:12px;font-weight:600;margin-top:16px">Read More</div></div>
<div class="abs" style="left:445px;top:3562px;width:310px">
  <div class="h-font" style="font-size:20px">Lorem ipsum dolor sit amet...</div>
  <div style="font-size:11px;color:#555;margin-top:10px">22 - June - 2022</div>
  <p class="para" style="margin-top:18px;line-height:22px">Lorem ipsum dolor sit amet, consectetur adipiscing elit, sed do eiusmod tempor incididunt ut labore....</p>
  <div class="h-font" style="font-size:12px;font-weight:600;margin-top:16px">Read More</div></div>
<div class="abs" style="left:789px;top:3562px;width:310px">
  <div class="h-font" style="font-size:20px">Lorem ipsum dolor sit amet...</div>
  <div style="font-size:11px;color:#555;margin-top:10px">22 - June - 2022</div>
  <p class="para" style="margin-top:18px;line-height:22px">Lorem ipsum dolor sit amet, consectetur adipiscing elit, sed do eiusmod tempor incididunt ut labore....</p>
  <div class="h-font" style="font-size:12px;font-weight:600;margin-top:16px">Read More</div></div>

<!-- footer -->
<div class="abs footer">
  <svg class="abs" style="left:100px;top:85px" width="28" height="26" viewBox="0 0 28 26"><rect x="2" y="8" width="24" height="16" rx="2" fill="none" stroke="#fff" stroke-width="2.4"/><path d="M2 9l12 8 12-8M6 8V2h16v6" fill="none" stroke="#fff" stroke-width="2.4"/></svg>
  <div class="abs h-font" style="left:151px;top:80px;font-size:26px;font-weight:500">Subscribe to our Newsletter</div>
  <div class="abs" style="left:617px;top:78px;width:482px;height:42px;border-radius:22px;background:#fff;color:#888;font-size:12px;padding:13px 24px">Your Email</div>
  <div class="btn dark" style="left:980px;top:78px;width:119px;height:42px;text-transform:none;font-weight:500;font-size:12px">Subscribe</div>

  <div class="abs" style="left:100px;top:196px;display:flex;align-items:center;gap:8px"><span style="width:34px;height:34px;border-radius:50%;background:#fff"></span><span class="h-font" style="font-size:17px;font-weight:600;line-height:1.05;width:150px">Meridian Acquisitions Group</span></div>
  <ul class="abs" style="left:100px;top:263px">
    <li>&#9742;&nbsp; +61-700-000-000</li>
    <li>&#9993;&nbsp; info@example.com</li>
    <li>&#9679;&nbsp; 18 Harbour Lane, Brisbane</li></ul>
  <h5 class="abs" style="left:392px;top:190px">Our Services</h5>
  <ul class="abs" style="left:392px;top:230px"><li>Selling a Business</li><li>Business Valuation</li><li>Business Acquisition</li><li>Capital Raising</li><li>Business Advisory</li></ul>
  <h5 class="abs" style="left:649px;top:190px">Usefull Link</h5>
  <ul class="abs" style="left:649px;top:230px"><li>Home</li><li>About Us</li><li>Business for Sale</li><li>Blog</li><li>Contact Us</li></ul>
  <h5 class="abs" style="left:880px;top:190px">Follow US</h5>
  <div class="abs" style="left:880px;top:228px;display:flex;gap:14px">
    <span style="width:28px;height:28px;border-radius:50%;border:1.5px solid #fff"></span><span style="width:28px;height:28px;border-radius:50%;border:1.5px solid #fff"></span><span style="width:28px;height:28px;border-radius:50%;border:1.5px solid #fff"></span><span style="width:28px;height:28px;border-radius:50%;border:1.5px solid #fff"></span></div>
  <p class="abs" style="left:880px;top:270px;width:220px;font-size:11.5px;line-height:20px">Lorem ipsum dolor sit amet, consectetur adipiscing elit, sed do eiusmod tempor incididunt ut labore....</p>
</div>
<div class="abs bar">
  <span class="abs" style="left:100px;top:18px">2022 All rights reserved</span>
  <span class="abs" style="left:880px;top:18px">Privacy Policy</span>
  <span class="abs" style="left:995px;top:18px">Terms &amp; Conditions</span>
</div>
</body>
</html>
```